P&H RESTORATION

I want a brochure similiar to the example i've attached.
My company name is P&H Restoration. The website is: P-H-Restoration.com.
The phone number is 803.417.9056.

I don't like the "yellow" being the main color of the example so I'm open to suggestions. I want something CLEAN & Simple, like our logo . This will be a bi fold brochure

```html
<!DOCTYPE html>
<html lang="en">
<head>
<meta charset="utf-8">
<title>P&amp;H Restoration – Bi-fold Brochure</title>
<link href="https://fonts.googleapis.com/css2?family=Poppins:wght@400;500;600;700&display=swap" rel="stylesheet">
<style>
:root{
  --navy-deep:#0c1a4f;
  --navy:#13286b;
  --royal:#1d3f95;
  --sky:#3f8ee0;
  --sky-light:#4b9cf0;
  --white:#ffffff;
  --paper:#f7f7f7;
  --ink:#101a3c;
  --grey:#8d9097;
  --page:#ffffff;
}
*{margin:0;padding:0;box-sizing:border-box}
html,body{width:1200px;height:2726px;overflow:hidden;background:var(--page)}
body{position:relative;font-family:"Poppins",sans-serif;color:var(--white)}
.spread{position:absolute;left:50px;width:988px;height:698px;transform-origin:0 0;transform:scale(1.1134);overflow:hidden;box-shadow:0 10px 40px rgba(0,0,0,.28)}
.spread--outside{top:390px}
.spread--inside{top:1557px}
.abs{position:absolute}
svg.abs{left:0;top:0}

/* outside */
.kitchen-photo{left:0;top:0;width:520px;height:475px;background:linear-gradient(160deg,#2a3a78 0%,#1a2a62 55%,#3a2a5a 100%)}
.worker-photo{left:500px;top:0;width:488px;height:611px;background:linear-gradient(200deg,#1e4aa6 0%,#173a8c 50%,#1a3f9a 100%)}
.contact-band{left:0;top:553px;width:988px;height:145px;background:var(--navy-deep)}
.claim-band{left:0;top:475px;width:470px;height:78px;background:var(--paper);border-bottom:6px solid #7b7f8a;padding:22px 0 0 26px;color:var(--ink)}
.claim-band .ask{font-weight:600;font-size:19px;line-height:1;letter-spacing:.2px}
.claim-band .team{font-weight:600;font-size:22px;line-height:1.15}
.brand{font-weight:600;color:var(--white);white-space:nowrap;display:flex;align-items:center}
.brand .mark{display:inline-block;border:2px solid var(--white);margin-right:12px}
.brand--small{left:30px;top:400px;font-size:22px}
.brand--small .mark{width:16px;height:16px}
.brand--large{left:648px;top:60px;font-size:34px}
.brand--large .mark{width:24px;height:24px}
.services{right:30px;top:418px;text-align:right}
.services li{list-style:none;font-weight:700;font-size:28px;line-height:1;padding:4px 0 8px;border-bottom:3px solid var(--white);margin-bottom:10px;display:flex;justify-content:flex-end;align-items:center;gap:14px}
.services li:nth-child(1){margin-left:140px}
.services svg{width:22px;height:22px}
.contacts{left:30px;top:588px;font-size:19px;line-height:26px}
.contacts div{display:flex;align-items:center;gap:20px}
.contacts svg{width:18px;height:18px}
.web-foot{left:640px;top:632px;font-size:17px;letter-spacing:2.6px}

/* inside */
.stone-bg{left:0;top:0;width:988px;height:698px;background:linear-gradient(135deg,#2d4488 0%,#243a7c 50%,#1e3372 100%)}
.trio{left:282px;top:56px;width:200px;text-align:center;font-size:28px;line-height:36px;font-weight:400}
.trio span{display:block}
.trio .mid{border-top:2px solid var(--white);border-bottom:2px solid var(--white)}
.headline{left:526px;top:50px;width:420px;text-align:center}
.headline h1{font-size:32px;font-weight:700;line-height:1.1;letter-spacing:-.3px}
.headline h2{font-size:22px;font-weight:600;color:var(--sky-light);letter-spacing:1.4px;line-height:1.3}
.steps{left:540px;top:160px;width:402px}
.step{position:relative;height:72px;margin-bottom:18px;display:flex}
.step .num{position:relative;width:80px;height:72px}
.step .num svg{position:absolute;left:0;top:0}
.step .body{flex:1;padding:6px 8px 0 8px;position:relative}
.step h3{font-size:13.5px;font-weight:500;line-height:1.1;letter-spacing:.2px}
.step p{font-size:9.6px;line-height:1.08;margin-top:2px}
.step .icon{position:absolute;right:12px;top:14px;width:44px;height:44px}
.step--light .body{background:var(--white);color:var(--ink)}
.step--light h3{color:var(--sky)}
.step--blue .body{background:var(--sky)}
.step--blue h3{color:var(--navy-deep)}
.step--blue p{color:var(--navy-deep)}
.brand--inside{left:694px;top:596px;font-size:30px}
.brand--inside .mark{width:22px;height:22px}
</style>
</head>
<body>

<section class="spread spread--outside">
  <div class="abs kitchen-photo" role="img" aria-label="Dim interior of a kitchen under renovation, tinted navy"></div>
  <div class="abs worker-photo" role="img" aria-label="Contractor in a plaid shirt working on plans, tinted royal blue"></div>
  <div class="abs contact-band"></div>
  <svg class="abs" width="988" height="698" viewBox="0 0 988 698">
    <rect x="500" y="611" width="488" height="87" fill="#0a1646"/>
    <polygon points="503,48 806,348 503,653 200,348" fill="#ffffff"/>
    <polygon points="503,60 794,348 503,641 212,348" fill="#2a4a9c"/>
    <polygon points="503,70 784,348 503,631 222,348" fill="#ffffff"/>
    <polygon points="503,80 774,348 503,621 232,348" fill="#c7a586" role="img" aria-label="City skyline of high-rise towers at sunset"/>
    <polygon points="503,80 774,348 503,350 232,348" fill="#b9cbe0"/>
  </svg>
  <div class="abs claim-band">
    <div class="ask">INSURANCE CLAIMED?</div>
    <div class="team">We’re on your team.</div>
  </div>
  <div class="abs brand brand--small"><span class="mark"></span>P&amp;H Restoration</div>
  <div class="abs brand brand--large"><span class="mark"></span>P&amp;H Restoration</div>
  <ul class="abs services">
    <li>BUILD <svg viewBox="0 0 22 22" fill="none" stroke="#fff" stroke-width="1.6"><rect x="6" y="3" width="8" height="17"/><path d="M14 10h4v10M3 20h17"/></svg></li>
    <li>RENOVATION <svg viewBox="0 0 22 22" fill="none" stroke="#fff" stroke-width="1.6"><path d="M3 11l8-7 8 7M5 9v11h12V9"/></svg></li>
    <li>RESTORATION <svg viewBox="0 0 22 22" fill="none" stroke="#fff" stroke-width="1.6"><rect x="3" y="3" width="16" height="16"/><path d="M3 9h16M3 14h16M9 3v16"/></svg></li>
  </ul>
  <div class="abs contacts">
    <div><svg viewBox="0 0 18 18" fill="none" stroke="#fff" stroke-width="1.4"><circle cx="9" cy="9" r="8"/><path d="M6 5l2 2-1 1.5 2.5 2.5L11 10l2 2-1.5 1.5C9 13 5 9 5 6.5z"/></svg>803-417-9056</div>
    <div><svg viewBox="0 0 18 18" fill="none" stroke="#fff" stroke-width="1.4"><circle cx="9" cy="9" r="8"/><path d="M1 9h16M9 1c3 3 3 13 0 16M9 1c-3 3-3 13 0 16"/></svg>www.P-H-Restoration.com</div>
    <div><svg viewBox="0 0 18 18" fill="none" stroke="#fff" stroke-width="1.4"><circle cx="9" cy="9" r="8"/><rect x="4.5" y="6" width="9" height="6"/><path d="M4.5 6l4.5 3.5L13.5 6"/></svg>info@P-H-Restoration.com</div>
  </div>
  <div class="abs web-foot">www.P-H-Restoration.com</div>
</section>

<section class="spread spread--inside">
  <div class="abs stone-bg" role="img" aria-label="Navy stone wall texture"></div>
  <svg class="abs" width="988" height="698" viewBox="0 0 988 698">
    <polygon points="0,0 138,0 472,335 90,698 0,698" fill="#8b8e95" role="img" aria-label="Black and white city skyline with a tower under construction"/>
    <polygon points="217,105 452,335 217,568 -18,335" fill="#13286b"/>
    <polygon points="217,120 437,335 217,553 -3,335" fill="#3d78c4" role="img" aria-label="Couple embracing in front of a blue building"/>
    <polygon points="389,448 470,528 389,608 308,528" fill="#ffffff"/>
    <polygon points="389,458 460,528 389,598 318,528" fill="#7d8fa5" role="img" aria-label="Water flowing over a flooded surface"/>
    <polygon points="285,540 365,620 285,698 205,620" fill="#ffffff"/>
    <polygon points="285,550 355,620 285,690 215,620" fill="#b7c7d6" role="img" aria-label="Industrial ductwork on a rooftop"/>
    <polygon points="497,545 652,698 342,698" fill="#ffffff"/>
    <polygon points="497,558 638,698 356,698" fill="#a9a29a" role="img" aria-label="Renovated open-plan kitchen interior"/>
  </svg>
  <div class="abs trio"><span>BUILD</span><span class="mid">RENOVATE</span><span>RESTORE</span></div>
  <div class="abs headline">
    <h1>Water or Mold Damage?</h1>
    <h2>What happens after cleanup?</h2>
  </div>
  <div class="abs steps">
    <div class="step step--light">
      <div class="num"><svg width="80" height="92" viewBox="0 0 80 92"><polygon points="0,0 80,0 80,72 40,92 0,72" fill="#fff"/><circle cx="40" cy="38" r="17" fill="none" stroke="#0c1a4f" stroke-width="3"/><text x="40" y="47" text-anchor="middle" font-family="Poppins,sans-serif" font-size="24" font-weight="500" fill="#0c1a4f">1</text></svg></div>
      <div class="body"><h3>DUCTWORK CLEANING</h3><p>Improving air quality in your home<br>Keep the air quality in your home clean. Cleaning<br>your air ducts can help minimize allergies, asthma,<br>and other sicknesses related to poor air quality.</p>
        <svg class="icon" viewBox="0 0 44 44" fill="#0c1a4f"><path d="M14 6h16v10H14z"/><path d="M6 18h32v6H6z"/><path d="M16 30c2 2-2 4 0 6M22 30c2 2-2 4 0 6M28 30c2 2-2 4 0 6" fill="none" stroke="#0c1a4f" stroke-width="1.6"/></svg></div>
    </div>
    <div class="step step--blue">
      <div class="num"><svg width="80" height="92" viewBox="0 0 80 92"><polygon points="0,0 80,0 80,72 40,92 0,72" fill="#3f8ee0"/><circle cx="40" cy="38" r="17" fill="none" stroke="#0c1a4f" stroke-width="3"/><text x="40" y="47" text-anchor="middle" font-family="Poppins,sans-serif" font-size="24" font-weight="500" fill="#0c1a4f">2</text></svg></div>
      <div class="body"><h3>DRYER VENT CLEANING</h3><p>Get a plugged dryer vent cleaned today!<br>A clogged dryer vent can cost you loads of money<br>through high electricity bills and dryer over heating.</p>
        <svg class="icon" viewBox="0 0 44 44" fill="none" stroke="#0c1a4f" stroke-width="2"><rect x="6" y="4" width="28" height="34" rx="2"/><path d="M6 11h28"/><circle cx="20" cy="25" r="8"/></svg></div>
    </div>
    <div class="step step--light">
      <div class="num"><svg width="80" height="92" viewBox="0 0 80 92"><polygon points="0,0 80,0 80,72 40,92 0,72" fill="#fff"/><circle cx="40" cy="38" r="17" fill="none" stroke="#0c1a4f" stroke-width="3"/><text x="40" y="47" text-anchor="middle" font-family="Poppins,sans-serif" font-size="24" font-weight="500" fill="#0c1a4f">3</text></svg></div>
      <div class="body"><h3>WATER DAMAGE RESTORATION</h3><p>When Water Damage Happens Call Us!<br>No one wants to deal with the headache with water<br>damage. Unexpected leaks or broken pipes simply<br>never occur at a convenient time.</p>
        <svg class="icon" viewBox="0 0 44 44" fill="#0c1a4f"><rect x="18" y="4" width="8" height="6"/><rect x="12" y="10" width="28" height="8" rx="2"/><rect x="8" y="14" width="10" height="14" rx="2"/><path d="M13 32c-3 4-3 7 0 7s3-3 0-7z"/></svg></div>
    </div>
    <div class="step step--blue">
      <div class="num"><svg width="80" height="92" viewBox="0 0 80 92"><polygon points="0,0 80,0 80,72 40,92 0,72" fill="#3f8ee0"/><circle cx="40" cy="38" r="17" fill="none" stroke="#0c1a4f" stroke-width="3"/><text x="40" y="47" text-anchor="middle" font-family="Poppins,sans-serif" font-size="24" font-weight="500" fill="#0c1a4f">4</text></svg></div>
      <div class="body"><h3>MOLD DAMAGE RESTORATION</h3><p>Mold Remediation that gets done right. Mold can<br>develop in almost any home or office is a very small<br>amount of time and moisture.</p>
        <svg class="icon" viewBox="0 0 44 44" fill="none" stroke="#0c1a4f" stroke-width="2.4"><circle cx="22" cy="22" r="11"/><path d="M22 4v7M22 33v7M4 22h7M33 22h7M9 9l5 5M30 30l5 5M35 9l-5 5M14 30l-5 5"/><circle cx="19" cy="19" r="2" fill="#0c1a4f"/><circle cx="25" cy="25" r="2" fill="#0c1a4f"/></svg></div>
    </div>
  </div>
  <div class="abs brand brand--inside"><span class="mark"></span>P&amp;H Restoration</div>
</section>

</body>
</html>
```